Silver MarlinJuice Company from Germany needs a Web Design

Hey Guys,

We need a Great Web Design I Hope we get nice Designs.
I put our company Logo in the Files.
Our Juice is Very Healthy and we don't use Sugar or other stuff it's 100% Natural Juice.
We are a German Company
Updates

I have a good Design already , but when someone works on a design, i will wait until you send it to me.

Industry/Entity Type

It Company

Coding

Coded - Design and coding required

Number of Pages Required

1 page

Requirements
Must have
• It has to be something with Vegetables: Apple, Carrots, courgette, fennel, beetroot, orange, salads, lemons, nettle. We producing the juice with these Vegetables and fruits.
Nice to have
• I Put a couple designs in the files i like Designs ,when you go on a Website and you are not confused :)

```html
<!DOCTYPE html>
<html lang="en">
<head>
<meta charset="utf-8">
<title>Silver Marlin Juice Company</title>
<link href="https://fonts.googleapis.com/css2?family=Open+Sans:wght@400;600;700;800&display=swap" rel="stylesheet">
<style>
:root{
  --green:#5aa529;
  --green-dark:#3f8a1d;
  --green-light:#7cc23a;
  --ink:#3b3b3b;
  --muted:#7a7a7a;
  --cream:#f6f1e6;
  --white:#ffffff;
}
*{box-sizing:border-box;margin:0;padding:0}
html,body{width:855px;height:1200px;overflow:hidden;background:var(--white)}
body{font-family:"Open Sans",Arial,sans-serif;color:var(--ink);position:relative}
.page{position:relative;width:855px;height:1200px;overflow:hidden}

/* header */
.site-nav{position:absolute;top:0;left:0;width:855px;height:34px;background:linear-gradient(var(--green-light),var(--green));z-index:3;display:flex;justify-content:space-between;padding:0 150px}
.nav-group{display:flex;gap:4px;align-items:center}
.nav-group a{color:var(--white);font-size:9.5px;font-weight:600;text-decoration:none;padding:11px 9px;letter-spacing:.3px}
.nav-group a.active{background:var(--green-dark)}
.brand{position:absolute;top:4px;left:382px;width:92px;height:92px;border-radius:50%;background:var(--white);z-index:4;display:flex;align-items:center;justify-content:center;text-align:center;box-shadow:0 2px 6px rgba(0,0,0,.2)}
.brand span{font-size:12px;font-weight:700;color:var(--green-dark);line-height:1.15}

/* hero */
.hero{position:absolute;top:0;left:0;width:855px;height:415px}
.hero-photo{position:absolute;inset:0;background:radial-gradient(circle at 290px 240px,#f07a22 0,#e8631a 70px,transparent 150px),radial-gradient(circle at 700px 120px,#e0b13a 0,transparent 120px),linear-gradient(180deg,#7fb0d9 0%,#b9d3e9 45%,#e9eef0 70%,#7c9b46 100%)}
.hero-copy{position:absolute;top:180px;width:100%;text-align:center;color:var(--white);text-shadow:0 2px 4px rgba(0,0,0,.35)}
.hero-copy h1{font-size:36px;font-weight:800;letter-spacing:.5px}
.hero-copy p{font-size:20px;font-weight:700;letter-spacing:1px;margin-top:4px}
.hero-btn{display:inline-block;margin-top:12px;background:var(--green);color:var(--white);font-size:9px;font-weight:700;padding:7px 16px;border-radius:3px;text-shadow:none}
.hero-arrow{position:absolute;top:214px;width:32px;height:32px;border-radius:50%;background:rgba(255,255,255,.85)}

/* welcome */
.welcome{position:absolute;top:415px;left:0;width:855px;height:290px;text-align:center}
.section-title{font-size:20px;font-weight:400;color:var(--ink)}
.welcome .section-title{margin-top:28px}
.welcome p{width:540px;margin:12px auto 0;font-size:8px;line-height:1.55;color:var(--muted)}
.features{display:flex;justify-content:center;gap:46px;margin-top:26px}
.feature{width:92px;height:92px;border-radius:50%;background:radial-gradient(circle at 40% 35%,var(--green-light),var(--green-dark));border:3px solid #e4efd9;display:flex;flex-direction:column;align-items:center;justify-content:center;color:var(--white);font-size:10px;font-weight:600;gap:6px}

/* benefits */
.benefits{position:absolute;top:690px;left:0;width:855px;height:215px;background:var(--cream)}
.benefits-wave{position:absolute;top:-40px;left:0}
.benefits-copy{position:absolute;left:160px;top:28px;width:330px}
.benefits-copy .section-title{font-size:19px}
.benefits-copy p{font-size:7.5px;line-height:1.55;color:var(--muted);margin-top:8px}
.benefit-list{list-style:none;margin-top:10px}
.benefit-list li{font-size:7.5px;color:var(--muted);display:flex;align-items:center;gap:6px;margin-bottom:5px}
.benefit-photo{position:absolute;left:505px;top:30px;width:320px;height:180px;border-radius:40px;background:radial-gradient(circle at 30% 55%,#d8402a 0,transparent 55px),radial-gradient(circle at 70% 40%,#f2a52a 0,transparent 60px),radial-gradient(circle at 55% 80%,#6aa83a 0,transparent 60px),#f0e4cc}

/* testimonial */
.testimonial{position:absolute;top:905px;left:0;width:855px;height:210px;text-align:center}
.testimonial .section-title{margin-top:18px;font-size:19px}
.testimonial blockquote{width:520px;margin:22px auto 0;font-size:8px;line-height:1.7;color:var(--muted);font-style:italic;position:relative}
.quote-mark{position:absolute;top:-14px;left:-28px;font-size:40px;color:#bbb;font-style:normal;font-family:Georgia,serif}
.customer{display:flex;align-items:center;justify-content:center;gap:8px;margin-top:14px}
.customer-photo{width:28px;height:28px;border-radius:50%;background:#c9a88e}
.customer-name{font-size:8px;font-weight:700;text-align:left}
.customer-name small{display:block;font-weight:400;color:var(--muted);font-size:7px}

/* footer */
.site-footer{position:absolute;top:1118px;left:0;width:855px;height:82px;background:linear-gradient(var(--green-light),var(--green-dark));color:var(--white);padding:26px 165px 0}
.footer-links{font-size:8.5px;font-weight:600;letter-spacing:.3px}
.copyright{font-size:7px;margin-top:6px;opacity:.9}
.socials{position:absolute;right:170px;top:26px;display:flex;gap:10px}
.socials span{width:12px;height:12px;border-radius:50%;background:var(--white)}
</style>
</head>
<body>
<div class="page">

  <section class="hero">
    <div class="hero-photo" role="img" aria-label="Photo of ripe oranges hanging on a tree branch against a blue sky"></div>
    <div class="hero-arrow" style="left:128px"><svg width="32" height="32"><path d="M18 10l-6 6 6 6" stroke="#555" stroke-width="2.5" fill="none"/></svg></div>
    <div class="hero-arrow" style="left:690px"><svg width="32" height="32"><path d="M14 10l6 6-6 6" stroke="#555" stroke-width="2.5" fill="none"/></svg></div>
    <div class="hero-copy">
      <h1>100% NATURAL &amp; HEALTHY</h1>
      <p>MAURIS LACUS ET VESTIBULUM</p>
      <span class="hero-btn">VIEW OUR JUICE</span>
    </div>
  </section>

  <nav class="site-nav">
    <div class="nav-group"><a class="active">HOME</a><a>ABOUT US</a><a>OUR JUICES</a></div>
    <div class="nav-group"><a>WHY OUR JUICE</a><a>TESTIMONIALS</a><a>CONTACT</a></div>
  </nav>
  <div class="brand"><span>Silver Marlin<br>Juice Company</span></div>

  <section class="welcome">
    <h2 class="section-title">WELCOME TO SILVER MARLIN</h2>
    <p>Fresh juice pressed every morning from apples, carrots, beetroot, fennel and lemons grown by farms near our home in Germany. We add no sugar and nothing artificial, only pure fruit and vegetables bottled for you. Taste the difference that honest ingredients make in every glass you pour.</p>
    <div class="features">
      <div class="feature"><svg width="30" height="26" viewBox="0 0 30 26"><path d="M15 24S2 16 2 8a6.5 6.5 0 0113-2 6.5 6.5 0 0113 2c0 8-13 16-13 16z" fill="none" stroke="#fff" stroke-width="2"/></svg>Healthy</div>
      <div class="feature"><svg width="28" height="28" viewBox="0 0 28 28"><path d="M4 24C4 10 12 4 24 4c0 12-6 20-20 20zM4 24l12-12" fill="none" stroke="#fff" stroke-width="2"/></svg>Natural</div>
      <div class="feature"><svg width="28" height="28" viewBox="0 0 28 28"><circle cx="14" cy="14" r="11" fill="none" stroke="#fff" stroke-width="2"/><path d="M6 6l16 16" stroke="#fff" stroke-width="2"/></svg>No Sugar</div>
      <div class="feature"><svg width="30" height="26" viewBox="0 0 30 26"><path d="M3 12h24a12 12 0 01-24 0z" fill="none" stroke="#fff" stroke-width="2"/><circle cx="11" cy="8" r="3" fill="#fff"/><circle cx="18" cy="7" r="3" fill="#fff"/></svg>Vegetables</div>
    </div>
  </section>

  <section class="benefits">
    <svg class="benefits-wave" width="855" height="42" viewBox="0 0 855 42"><path d="M0 42C200 0 650 0 855 42z" fill="var(--cream)"/></svg>
    <div class="benefits-copy">
      <h2 class="section-title">What Benefits of Our Juice</h2>
      <p>Each bottle holds the goodness of whole fruit and vegetables, cold pressed to keep vitamins, minerals and flavour intact from farm to your table.</p>
      <ul class="benefit-list">
        <li><svg width="9" height="9"><circle cx="4.5" cy="4.5" r="4.5" fill="var(--green)"/><path d="M2.3 4.6l1.5 1.5 3-3" stroke="#fff" fill="none"/></svg>Rich in natural vitamins from fresh fruit and vegetables</li>
        <li><svg width="9" height="9"><circle cx="4.5" cy="4.5" r="4.5" fill="var(--green)"/><path d="M2.3 4.6l1.5 1.5 3-3" stroke="#fff" fill="none"/></svg>Free from added sugar and preservatives</li>
        <li><svg width="9" height="9"><circle cx="4.5" cy="4.5" r="4.5" fill="var(--green)"/><path d="M2.3 4.6l1.5 1.5 3-3" stroke="#fff" fill="none"/></svg>Supports digestion and a strong immune system</li>
        <li><svg width="9" height="9"><circle cx="4.5" cy="4.5" r="4.5" fill="var(--green)"/><path d="M2.3 4.6l1.5 1.5 3-3" stroke="#fff" fill="none"/></svg>Pressed daily from regional produce</li>
        <li><svg width="9" height="9"><circle cx="4.5" cy="4.5" r="4.5" fill="var(--green)"/><path d="M2.3 4.6l1.5 1.5 3-3" stroke="#fff" fill="none"/></svg>Delivered chilled straight to your door</li>
      </ul>
    </div>
    <div class="benefit-photo" role="img" aria-label="Photo of glasses of fresh juice surrounded by oranges, pomegranate, kiwi and vegetables"></div>
  </section>

  <section class="testimonial">
    <h2 class="section-title">What Our Customer Says</h2>
    <blockquote><span class="quote-mark">&ldquo;</span>Since I started my mornings with Silver Marlin juice I feel more awake and energetic all day. The carrot and apple blend is my favourite, and knowing there is no added sugar makes me happy to share it with my whole family every single week.</blockquote>
    <div class="customer">
      <div class="customer-photo" role="img" aria-label="Customer portrait"></div>
      <div class="customer-name">Lena Hartwig<small>Happy Customer</small></div>
    </div>
  </section>

  <footer class="site-footer">
    <div class="footer-links">HOME &nbsp;|&nbsp; ABOUT US &nbsp;|&nbsp; OUR JUICES &nbsp;|&nbsp; WHY OUR JUICE &nbsp;|&nbsp; TESTIMONIALS &nbsp;|&nbsp; CONTACT</div>
    <div class="copyright">&copy; 2024 Silver Marlin Juice Company. All rights reserved.</div>
    <div class="socials"><span></span><span></span><span></span></div>
  </footer>

</div>
</body>
</html>
```